Kestrow-Holdings. Limestone; improving the world

New Limestone company and need logo design.
Limestone offsets carbon mitigation industries restore and replenish soil fertilities in the Prairies, the breadbasket of the world. At the same time, Limestone is proving a critical emergent component of carbon capture sequestration technology will therefore play a critical role in the development of the western Canadian energy industries
Our limestone resources are situated in the foothills of the Canadian Rockies well-positioned above the sprawling fields of the vast peace district.
Target Market(s)
Agriculture and oli sites
Logo Text
Kestrow Holdings
Number of Pages Required
3 page

```html
<!DOCTYPE html>
<html lang="en">
<head>
<meta charset="utf-8">
<title>Kestrow Holdings</title>
<link href="https://fonts.googleapis.com/css2?family=Montserrat:wght@400;500;600;700;800&display=swap" rel="stylesheet">
<style>
:root{
  --green:#3fa34d;
  --ink:#111;
  --brown:#624839;
  --white:#fff;
  --hero-a:#d2b47a;
  --hero-b:#c6a262;
  --rule:rgba(255,255,255,.25);
}
*{box-sizing:border-box;margin:0;padding:0}
html,body{width:747px;height:1200px;overflow:hidden;background:var(--white)}
body{font-family:'Montserrat',sans-serif;color:var(--ink);position:relative}

.site-header{position:absolute;left:0;top:0;width:747px;height:52px;background:var(--white)}
.brand{position:absolute;display:flex;align-items:center;gap:8px;font-weight:700;letter-spacing:.3px}
.brand-mark{width:26px;height:26px;border-radius:50%;background:var(--green)}
.site-header .brand{left:100px;top:12px;font-size:12.5px}
.main-nav{position:absolute;top:20px;left:0;font-size:8.5px;font-weight:500;letter-spacing:.2px}
.main-nav a{position:absolute;white-space:nowrap;color:var(--ink);text-decoration:none}

.hero{position:absolute;left:0;top:52px;width:747px;height:340px;
  background:linear-gradient(180deg,var(--hero-a) 0%,var(--hero-b) 100%)}
.hero-title{position:absolute;left:0;width:747px;top:100px;text-align:center;font-size:28.5px;font-weight:800;letter-spacing:.2px}
.hero-sub{position:absolute;left:0;width:747px;top:137px;text-align:center;font-size:10.5px;font-weight:500;line-height:18px}

.about{position:absolute;left:0;top:392px;width:747px;height:575px;
  background:linear-gradient(180deg,#efefef 0%,#f6f6f6 45%,#fcfcfc 100%)}
.section-title{font-size:20px;font-weight:700;letter-spacing:.5px}
.about .section-title{position:absolute;left:0;width:747px;top:44px;text-align:center}
.about-copy{position:absolute;left:116px;width:515px;font-size:8.4px;line-height:15.2px;text-align:center}
.btn{position:absolute;background:var(--green);color:var(--white);font-size:8px;font-weight:600;
  display:flex;align-items:center;justify-content:center;letter-spacing:.2px}

.frame{position:absolute;left:90px;top:667px;width:246px;height:246px;border:3px solid var(--green)}
.photo-globe{position:absolute;left:100px;top:678px;width:253px;height:243px;
  background:linear-gradient(160deg,#a9cc74 0%,#8cbf5a 55%,#5e9e36 100%)}
.sust-title{position:absolute;left:382px;top:722px}
.sust-copy{position:absolute;left:382px;top:755px;width:262px;font-size:8.6px;line-height:16px}

.site-footer{position:absolute;left:0;top:967px;width:747px;height:203px;background:var(--brown);color:var(--white)}
.site-footer .brand{left:281px;top:33px;font-size:12.5px}
.site-footer .brand-mark{background:var(--white)}
.foot-nav{position:absolute;top:85px;left:0;font-size:9.5px;font-weight:500;letter-spacing:.4px}
.foot-nav span{position:absolute;white-space:nowrap}
.foot-nav .sep{color:rgba(255,255,255,.4)}
.foot-rule{position:absolute;left:100px;top:116px;width:546px;height:1px;background:var(--rule)}
.contact{position:absolute;top:135px;display:flex;gap:8px;font-size:10px;line-height:15.5px}
.contact-icon{width:25px;height:25px;border-radius:50%;background:var(--white);display:flex;align-items:center;justify-content:center;flex:none}
.vdiv{position:absolute;top:135px;width:1px;height:32px;background:var(--rule)}

.bottom-bar{position:absolute;left:0;top:1170px;width:747px;height:30px;background:var(--green);color:var(--white)}
.copyright{position:absolute;left:101px;top:10px;font-size:8px}
.social{position:absolute;top:7px;width:16px;height:16px;border:1px solid var(--white);border-radius:50%}
</style>
</head>
<body>

<header class="site-header">
  <div class="brand"><span class="brand-mark"></span>KESTROW HOLDINGS</div>
  <nav class="main-nav">
    <a style="left:410px">HOME</a>
    <a style="left:464px">ABOUT US</a>
    <a style="left:537px">FAQs</a>
    <a style="left:588px">CONTACT US</a>
  </nav>
</header>

<section class="hero" role="img" aria-label="Photograph of a golden prairie wheat field under a cloudy sky">
  <h1 class="hero-title">WE ARE LIMESTONE COMPANY</h1>
  <p class="hero-sub">We Offset Carbon Mitigation Industries Restore And Replenish Soil Fertilities In<br>The Prairies, The Breadbasket of The World</p>
</section>

<section class="about" role="img" aria-label="Faint background photograph of a young plant held in a hand">
  <h2 class="section-title">WHO WE ARE</h2>
  <p class="about-copy" style="top:79px">Vivamus nec eros sed dui bibendum placerat vel vel erat. Vestibulum sed lacus in lacus porta suscipit sit amet nec diam. diam erat, mollis ut hendrerit vitae, efficitur In ut urna iaculis, posuere mi vel, pellentesque ipsum.</p>
  <p class="about-copy" style="top:115px">Quisque lacinia, nisl nec elementum malesuada, magna nunc malesuada metus, id aliquet nisl diam et magna. Curabitur tempor ultrices libero id eleifend. Sed malesuada, orci non facilisis tincidunt, tellus tellus sollicitudin est, id semper quam ligula in justo. Vivamus quis semper metus. Vestibulum vestibulum ex est, id posuere sem malesuada eu. In purus elit, consectetur a lorem ultricies, ultrices dictum magna. Phasellus pharetra a sapien a scelerisque. Nunc pretium arcu ac<br>ipsum elementum, a mattis lacus condimentum. Donec ac pretium leo.</p>
  <a class="btn" style="left:334px;top:200px;width:79px;height:24px">READ MORE</a>
</section>

<div class="frame"></div>
<div class="photo-globe" role="img" aria-label="Photograph of a glass globe resting on green grass"></div>
<h2 class="section-title sust-title">SUSTAINABILITY</h2>
<p class="sust-copy">Lorem ipsum dolor sit amet, consectetur adipiscing elit as<br>phasellus molestie neque augue, eget blandit ex tincidunt<br>vitae. Donec tristique lacus eget auctor viverra. Interduim<br>et malesuada fames ac ante ipsum primis in faucibus maur<br>sed lacus at turpis convallis tincidunt at id lectus.</p>
<a class="btn" style="left:381px;top:848px;width:80px;height:23px">KNOW MORE</a>

<footer class="site-footer">
  <div class="brand"><span class="brand-mark"></span>KESTROW HOLDINGS</div>
  <nav class="foot-nav">
    <span style="left:208px">HOME</span>
    <span class="sep" style="left:266px">|</span>
    <span style="left:297px">ABOUT&nbsp; US</span>
    <span class="sep" style="left:380px">|</span>
    <span style="left:411px">FAQs</span>
    <span class="sep" style="left:466px">|</span>
    <span style="left:497px">CONTACT US</span>
  </nav>
  <div class="foot-rule"></div>

  <div class="contact" style="left:102px">
    <span class="contact-icon"><svg width="10" height="13" viewBox="0 0 10 13"><path d="M5 0a5 5 0 0 0-5 5c0 3.5 5 8 5 8s5-4.5 5-8a5 5 0 0 0-5-5z" fill="#3fa34d"/><circle cx="5" cy="5" r="1.8" fill="#fff"/></svg></span>
    <span>123, Building Name, Street<br>City, State XY 123456</span>
  </div>
  <div class="vdiv" style="left:280px"></div>

  <div class="contact" style="left:319px">
    <span class="contact-icon"><svg width="12" height="12" viewBox="0 0 12 12"><path d="M2.5 1l2 2.2-1 1.3c.7 1.5 1.8 2.6 3.3 3.3l1.3-1 2.2 2-1.2 1.8C5 10.5 1.5 7 .7 2.2z" fill="#3fa34d"/></svg></span>
    <span>Phone<br>+1 555 014 2290</span>
  </div>
  <div class="vdiv" style="left:466px"></div>

  <div class="contact" style="left:486px">
    <span class="contact-icon"><svg width="13" height="13" viewBox="0 0 13 13"><path d="M12.5.5L.5 5.5l4.5 1.8L6.8 12z" fill="#3fa34d"/></svg></span>
    <span style="padding-top:4px">Email<br>info@kestrowholdings.com</span>
  </div>
</footer>

<div class="bottom-bar">
  <p class="copyright">Copyright © 2021 KESTROW HOLDINGS. All Rights Reserved.</p>
  <span class="social" style="left:588px" aria-label="Social link"></span>
  <span class="social" style="left:609px" aria-label="Social link"></span>
  <span class="social" style="left:630px" aria-label="Social link"></span>
</div>

</body>
</html>
```